Infoblatt
Zielgruppe
Talentförderung, Personalentwicklung, Beratung von Personalabteilungen
Zielgruppe: Personaler, HR Verantwortliche
Aufgabenstellung
Es geht um einen "One-Pager", der auf einem Kongress ausgelegt werden soll und in Kurzform einen Überblick über unser Unternehmen und unser Angebot informieren soll.
Wir haben Visitenkarten auf Recyclingpapier und möchten das Blatt konsistent auf das gleiche Papier drucken lassen, daher einfarbig schwarz. Format DIN A4 Hoch.
IDEE: Vom Stil wie eine Infografik aufbauen
TYPO: unser LOGO ist BEBAS NEUE und unsere Schrift Helvetica

```html
<!DOCTYPE html>
<html lang="de">
<head>
<meta charset="utf-8">
<title>ANKERHAUS – Infoblatt</title>
<link rel="stylesheet" href="https://fonts.googleapis.com/css2?family=Roboto+Condensed:wght@300;400;700&display=swap">
<style>
  :root {
    --ink: #231f20;
    --paper: #ffffff;
    --arc-grey: #a7a9ac;
    --soft-grey: #9a9a9a;
    --accent-grey: #5a5a5a;
    --text: #1e1e1e;
  }
  * { margin: 0; padding: 0; box-sizing: border-box; }
  html, body { width: 891px; height: 1200px; overflow: hidden; background: var(--paper); }
  body { font-family: "Roboto Condensed", "Helvetica Neue", Arial, sans-serif; color: var(--text); }

  .sheet { position: relative; width: 891px; height: 1200px; background: var(--paper); overflow: hidden; }

  .brand-name { position: absolute; left: 0; top: 0; width: 150px; height: 540px; }
  .brand-name text {
    font-family: "Roboto Condensed", "Helvetica Neue", Arial, sans-serif;
    font-weight: 700; font-size: 118px; fill: var(--ink);
  }
  .brand-url {
    position: absolute; left: 22px; top: 34px; height: 160px; width: 18px;
    writing-mode: vertical-rl; transform: rotate(180deg);
    font-weight: 300; font-size: 13px; line-height: 18px; color: var(--soft-grey);
    text-align: end; white-space: nowrap;
  }

  .arc-shape { position: absolute; left: 0; top: 0; width: 891px; height: 520px; }

  .heading { position: absolute; font-weight: 700; color: var(--ink); line-height: 1; white-space: nowrap; }
  .heading--mission { left: 186px; top: 34px; font-size: 32px; }
  .heading--story { right: 41px; top: 124px; font-size: 30px; }
  .heading--credo { left: 52px; top: 597px; font-size: 31px; color: var(--paper); }
  .heading--mehrwert { left: 540px; top: 771px; font-size: 33px; }
  .heading--mehrwert .soft { color: var(--accent-grey); }

  .line { position: absolute; white-space: nowrap; font-size: 15.5px; line-height: 20px; }
  .line.just { text-align: justify; text-align-last: justify; }
  .story .line { right: 36px; }

  .credo-band {
    position: absolute; left: 0; top: 571px; width: 858px; height: 138px; background: var(--ink);
  }
  .credo-text {
    position: absolute; left: 52px; top: 650px;
    font-size: 17px; line-height: 21px; color: var(--paper); white-space: nowrap;
  }

  .team-photo {
    position: absolute; left: 0; top: 716px; width: 541px; height: 484px;
    background:
      radial-gradient(ellipse 60% 45% at 45% 65%, rgba(70,70,70,0.75), rgba(140,140,140,0.35) 55%, rgba(255,255,255,0) 80%),
      linear-gradient(180deg, #ffffff 0%, #ececec 30%, #c9c9c9 65%, #e6e6e6 100%);
    -webkit-mask-image: linear-gradient(90deg, #000 70%, transparent 100%);
    mask-image: linear-gradient(90deg, #000 70%, transparent 100%);
  }

  .offer { position: absolute; left: 540px; font-size: 15.5px; line-height: 21px; white-space: nowrap; }
  .offer-intro { top: 842px; }
  .offer-label--business { top: 927px; }
  .offer-label--youth { top: 1073px; }
  .offer-list { list-style: none; }
  .offer-list--business { top: 968px; }
  .offer-list--youth { top: 1114px; }
  .offer-list li { position: relative; padding-left: 26px; line-height: 20.5px; }
  .offer-list li::before {
    content: ""; position: absolute; left: 2px; top: 7px; width: 7px; height: 7px;
    border-radius: 50%; background: var(--ink);
  }
</style>
</head>
<body>
<main class="sheet">
  <svg class="arc-shape" viewBox="0 0 891 520" aria-hidden="true">
    <path d="M891 74 A 690 690 0 0 0 234 512 L 891 512 Z" fill="var(--arc-grey)"/>
  </svg>

  <div class="brand-url">www.ankerhaus.de</div>
  <svg class="brand-name" viewBox="0 0 150 540" role="img" aria-label="ANKERHAUS">
    <text transform="translate(134,530) rotate(-90)" x="0" y="0" textLength="497" lengthAdjust="spacingAndGlyphs">ANKERHAUS</text>
  </svg>

  <section class="mission">
    <h2 class="heading heading--mission">Mission</h2>
    <div class="line just" style="left:186px;top:94px;width:398px">Kundare heißt marktschreierisch anpreisen, hinters Licht</div>
    <div class="line just" style="left:186px;top:114px;width:342px">führen, täuschen. Mandare heißt beauftragen,</div>
    <div class="line just" style="left:186px;top:135px;width:298px">Vertrauen schenken. Wir legen großen Wert</div>
    <div class="line" style="left:186px;top:155px">auf eine Beziehung, die Mandare, nicht</div>
    <div class="line" style="left:186px;top:176px">Kundare entspricht. Für uns ist der</div>
    <div class="line just" style="left:186px;top:196px;width:200px">partnerschaftliche Umgang</div>
    <div class="line just" style="left:186px;top:217px;width:176px">mit unseren Mandanten</div>
    <div class="line just" style="left:186px;top:237px;width:157px">das Fundament. Wir</div>
    <div class="line" style="left:186px;top:258px">haben keine Kunden.</div>
    <div class="line just" style="left:186px;top:278px;width:122px">Wir unterstützen</div>
    <div class="line" style="left:186px;top:299px">Mandanten.</div>
  </section>

  <section class="story">
    <h2 class="heading heading--story">Story</h2>
    <div class="line just" style="top:187px;left:534px">Meistens erwachen gute Ideen nicht im</div>
    <div class="line just" style="top:210px;left:497px">Kopf, sondern im Bauch. Voller Leidenschaft und</div>
    <div class="line just" style="top:233px;left:464px">Enthusiasmus, haben wir uns 2006 unseren persönlichen</div>
    <div class="line just" style="top:255px;left:434px">Freiraum geschaffen. Nur im Freiraum entsteht etwas. Hier</div>
    <div class="line just" style="top:278px;left:408px">können Kompetenzen wachsen und Ideen reifen. Als ehemalige</div>
    <div class="line just" style="top:301px;left:386px">Personaler wussten wir schon bei der Gründung, inwieweit ein externer</div>
    <div class="line just" style="top:324px;left:366px">Berater Unternehmen unterstützen kann und sollte, gleichzeitig kannten</div>
    <div class="line just" style="top:347px;left:348px">wir die Grenzen dieser Verbindung. Die Tücken liegen in der Umsetzung</div>
    <div class="line just" style="top:369px;left:333px">- nämlich dann, wenn der Berater nicht mehr im Haus ist. Bis heute haben</div>
    <div class="line just" style="top:392px;left:318px">wir keine Schubladen, aus denen wir unsere Antwortkonzepte ziehen. Jeder</div>
    <div class="line just" style="top:415px;left:304px">Auftrag bedeutet für uns viele Gedanken, viel Analyse und somit sehr viel Herzblut.</div>
    <div class="line just" style="top:438px;left:294px">Mittlerweile sind wir in unserem festen Kernteam zu sechst und fokussieren uns auf</div>
    <div class="line" style="top:461px;left:283px;right:auto">das Thema Talent und Talentförderung.</div>
  </section>

  <section class="credo">
    <div class="credo-band"></div>
    <h2 class="heading heading--credo">Credo</h2>
    <p class="credo-text">Wir glauben, dass sich persönliche und ökonomische Werte ergänzen - mehr noch, dass sie langfristig nicht<br>ohne einander auskommen und dass sich emotionale Bindung als Mehrwert in Zahlen ausdrückt.</p>
  </section>

  <div class="team-photo" role="img" aria-label="Schwarzweißfoto: Team im Gespräch in einem hellen Büro, bewegungsunscharf"></div>

  <section class="mehrwert">
    <h2 class="heading heading--mehrwert">Mehr<span class="soft">wert</span></h2>
    <p class="offer offer-intro">Wir beraten Unternehmen im Rahmen der<br>Talentförderung und helfen Jugendlichen<br>auf dem Weg in ihr Berufsleben.</p>
    <p class="offer offer-label--business">Für Unternehmen:</p>
    <ul class="offer offer-list offer-list--business">
      <li>Talentförderung &amp; Talent Management</li>
      <li>Professionalisierung der Personalarbeit</li>
      <li>Organisationsentwicklung</li>
      <li>Potentialorientierte Mitarbeiterführung</li>
    </ul>
    <p class="offer offer-label--youth">Für die junge Generation:</p>
    <ul class="offer offer-list offer-list--youth">
      <li>Berufsorientierung</li>
      <li>Bewerbungscoaching</li>
    </ul>
  </section>
</main>
</body>
</html>
```